Updated Buisness card/Design

Target Market(s)

Residential clients

Industry/Entity Type

Interior remodeling

Contact Information for Business Card

see mark up

Requirements
Must have
• Logo

```html
<!DOCTYPE html>
<html lang="en">
<head>
<meta charset="utf-8">
<title>Verdeza Remodeling Group – Business Card</title>
<link href="https://fonts.googleapis.com/css2?family=Lato:wght@300;400;700;900&display=swap" rel="stylesheet">
<style>
  :root{
    --brand-blue:#3a9fdb;
    --slate:#7b818a;
    --ink:#6d7179;
    --paper:#ffffff;
    --backdrop:#e9ebee;
  }
  *{box-sizing:border-box;margin:0;padding:0}
  html,body{width:1200px;height:952px;overflow:hidden;background:var(--backdrop)}
  body{font-family:"Lato",sans-serif;position:relative}
  .card{
    position:absolute;top:321px;width:540px;height:310px;border-radius:18px;overflow:hidden;
    box-shadow:0 6px 18px rgba(0,0,0,.12);
  }
  .card--front{left:40px;background:var(--paper)}
  .card--back{left:620px;background:var(--brand-blue)}

  .front-graphics{position:absolute;inset:0}

  .wordmark{position:absolute;display:flex;align-items:center;gap:10px;white-space:nowrap}
  .wordmark__square{width:14px;height:14px;background:var(--brand-blue);flex:none}
  .wordmark__name{font-weight:900;text-transform:uppercase;line-height:1.1;letter-spacing:.5px}
  .card--front .wordmark{left:30px;top:112px}
  .card--front .wordmark__name{color:var(--slate);font-size:19px}
  .card--back .wordmark{left:50%;top:100px;transform:translateX(-50%)}
  .card--back .wordmark__square{width:16px;height:16px;background:var(--paper)}
  .card--back .wordmark__name{color:var(--paper);font-size:28px}

  .person{position:absolute;left:300px;top:46px}
  .person__name{font-size:26px;color:var(--brand-blue);letter-spacing:.5px;line-height:1;white-space:nowrap}
  .person__first{font-weight:400}
  .person__last{font-weight:900}
  .person__title{font-size:12.5px;color:var(--ink);margin-top:5px}
  .person__rule{width:70px;height:2px;background:var(--brand-blue);margin-top:6px}

  .contacts{position:absolute;left:282px;top:122px;list-style:none}
  .contacts li{display:flex;align-items:flex-start;gap:8px;font-size:12.5px;color:var(--ink);line-height:1.3;margin-bottom:5px}
  .contacts .icon{width:16px;height:16px;flex:none;margin-top:1px}

  .license{position:absolute;left:290px;bottom:14px;font-size:14px;color:var(--paper);letter-spacing:.2px}

  .services{position:absolute;left:0;right:0;top:196px;text-align:center;color:var(--paper);font-size:12.5px;line-height:1.5}
</style>
</head>
<body>

<section class="card card--front" aria-label="Business card front">
  <svg class="front-graphics" width="540" height="310" viewBox="0 0 540 310">
    <polyline points="0,184 236,184 262,262" fill="none" stroke="var(--slate)" stroke-width="2.5"/>
    <polygon points="256,262 540,262 540,310 272,310" fill="var(--brand-blue)"/>
  </svg>

  <div class="wordmark">
    <span class="wordmark__square"></span>
    <span class="wordmark__name">Verdeza<br>Remodeling Group</span>
  </div>

  <div class="person">
    <p class="person__name"><span class="person__first">MARCUS</span> <span class="person__last">ELLERY</span></p>
    <p class="person__title">Managing Director</p>
    <div class="person__rule"></div>
  </div>

  <ul class="contacts">
    <li>
      <svg class="icon" viewBox="0 0 16 16"><rect width="16" height="16" rx="3" fill="var(--brand-blue)"/><path d="M8 3a3.3 3.3 0 0 0-3.3 3.3C4.7 9 8 13 8 13s3.3-4 3.3-6.7A3.3 3.3 0 0 0 8 3zm0 4.6a1.3 1.3 0 1 1 0-2.6 1.3 1.3 0 0 1 0 2.6z" fill="#fff"/></svg>
      <span>482 Orchard View Rd Suite 210<br>Palm Ridge, CA 90000</span>
    </li>
    <li>
      <svg class="icon" viewBox="0 0 16 16"><rect width="16" height="16" rx="3" fill="var(--brand-blue)"/><path d="M5.2 3.5l1.6 2.3-1 1a6 6 0 0 0 3.4 3.4l1-1 2.3 1.6-.9 1.7C7.5 12.3 3.7 8.5 3.5 4.4z" fill="#fff"/></svg>
      <span>555.214.0387</span>
    </li>
    <li>
      <svg class="icon" viewBox="0 0 16 16"><rect width="16" height="16" rx="3" fill="var(--brand-blue)"/><rect x="5" y="2.8" width="6" height="10.4" rx="1" fill="#fff"/><rect x="6" y="4" width="4" height="6.5" fill="var(--brand-blue)"/></svg>
      <span>555.214.0388</span>
    </li>
    <li>
      <svg class="icon" viewBox="0 0 16 16"><rect width="16" height="16" rx="3" fill="var(--brand-blue)"/><rect x="3" y="4.5" width="10" height="7" fill="#fff"/><path d="M3 4.5l5 4 5-4" fill="none" stroke="var(--brand-blue)" stroke-width="1"/></svg>
      <span>marcus@verdezaremodel.com</span>
    </li>
    <li>
      <svg class="icon" viewBox="0 0 16 16"><rect width="16" height="16" rx="3" fill="var(--brand-blue)"/><path d="M5 3.5l6.5 5-3 .4 1.6 3.2-1.2.6-1.6-3.2L5 11.5z" fill="#fff"/></svg>
      <span>www.verdezaremodel.com</span>
    </li>
  </ul>

  <p class="license">CA Contractors License - 123456</p>
</section>

<section class="card card--back" aria-label="Business card back">
  <div class="wordmark">
    <span class="wordmark__square"></span>
    <span class="wordmark__name">Verdeza<br>Remodeling Group</span>
  </div>
  <p class="services">Design-Build Services • Project Management • Kitchen &amp; Bath Remodeling<br>Specialty Services: Cabinets • Carpentry • Flooring • Tile • Stone</p>
</section>

</body>
</html>
```